Redesign of business card for Birchline Mechanical

We are looking for a new design for our business cards for Birchline Mechanical. We are a plumbing & HVAC construction company, operating on the West Coast of Canada and USA. Logo attached.
Industry/Entity Type
Construction - Plumbing & HVAC
Contact Information for Business Card
Name, address, phone numbers, email, website address
Look and feel
Each slider illustrates characteristics of the customer's brand and the style your logo design should communicate.

```html
<!DOCTYPE html>
<html lang="en">
<head>
<meta charset="utf-8">
<title>Birchline Mechanical – Business Card</title>
<link href="https://fonts.googleapis.com/css2?family=Barlow+Condensed:wght@400;500;600&display=swap" rel="stylesheet">
<style>
  :root {
    --bg: #ececec;
    --ink: #000000;
    --paper: #ffffff;
    --pattern-a: #0a0a0a;
    --pattern-b: #1c1c1c;
    --rule: #8a8a8a;
  }
  * { box-sizing: border-box; margin: 0; padding: 0; }
  html, body { width: 1102px; height: 1200px; overflow: hidden; background: var(--bg); }
  body { position: relative; font-family: "Barlow Condensed", "Arial Narrow", sans-serif; color: var(--ink); }

  .card { position: absolute; left: 176px; width: 763px; height: 436px; border-radius: 14px; overflow: hidden; }

  /* Front */
  .card-front { top: 123px; background: var(--ink); }
  .front-pattern { position: absolute; inset: 0; background: radial-gradient(ellipse at center, var(--pattern-b), var(--pattern-a) 70%); }
  .front-brand { position: absolute; left: 0; right: 0; top: 190px; display: flex; justify-content: center; align-items: center; gap: 16px; color: var(--paper); }
  .front-brand .mark { width: 30px; height: 30px; background: var(--paper); }
  .front-brand .name { font-size: 40px; font-weight: 500; letter-spacing: 1.5px; text-transform: uppercase; line-height: 1; }

  /* Back */
  .card-back { top: 631px; background: var(--paper); }
  .back-frame { position: absolute; inset: 0; }
  .company-name { position: absolute; left: 28px; top: 60px; font-size: 36px; font-weight: 500; letter-spacing: 1.5px; text-transform: uppercase; line-height: 1; }
  .back-brand { position: absolute; right: 28px; top: 64px; display: flex; align-items: center; gap: 10px; }
  .back-brand .mark { width: 22px; height: 22px; background: var(--ink); }
  .back-brand .name { font-size: 30px; font-weight: 600; letter-spacing: 1px; text-transform: uppercase; line-height: 1; }

  .person-name { position: absolute; left: 52px; top: 182px; font-size: 31px; font-weight: 500; letter-spacing: 1.5px; text-transform: uppercase; line-height: 1; }
  .person-title { position: absolute; left: 52px; top: 226px; font-size: 16px; letter-spacing: 1px; text-transform: uppercase; line-height: 1; }
  .divider-h { position: absolute; left: 28px; width: 710px; top: 265px; height: 1px; background: var(--rule); }
  .divider-v { position: absolute; left: 382px; top: 296px; width: 1px; height: 111px; background: var(--ink); }

  .contact { position: absolute; display: flex; align-items: center; font-size: 18px; letter-spacing: 1px; line-height: 1; }
  .contact svg { width: 22px; height: 22px; position: absolute; left: 0; }
  .contact span { position: absolute; white-space: nowrap; }
  .contact-left { left: 50px; }
  .contact-left span { left: 57px; }
  .contact-right { left: 466px; }
  .contact-right span { left: 62px; text-transform: uppercase; }
  .contact-right span.lower { text-transform: none; }
</style>
</head>
<body>

<section class="card card-front">
  <div class="front-pattern" role="img" aria-label="Repeating outline monogram pattern in fine grey lines on black"></div>
  <div class="front-brand">
    <div class="mark"></div>
    <div class="name">Birchline Mechanical</div>
  </div>
</section>

<section class="card card-back">
  <svg class="back-frame" width="763" height="436" viewBox="0 0 763 436">
    <rect x="4" y="4" width="755" height="428" rx="11" fill="none" stroke="#000" stroke-width="8"/>
    <rect x="28" y="0" width="7" height="9" fill="#fff"/>
    <rect x="571" y="0" width="7" height="9" fill="#fff"/>
    <rect x="220" y="427" width="7" height="9" fill="#fff"/>
    <rect x="727" y="427" width="7" height="9" fill="#fff"/>
  </svg>

  <div class="company-name">Birchline Mechanical</div>
  <div class="back-brand">
    <div class="mark"></div>
    <div class="name">Birchline</div>
  </div>

  <div class="person-name">Your Full Name</div>
  <div class="person-title">Title</div>
  <div class="divider-h"></div>
  <div class="divider-v"></div>

  <div class="contact contact-left" style="top:297px;">
    <svg viewBox="0 0 22 22" fill="none" stroke="#000" stroke-width="1.5"><rect x="6" y="1.5" width="10" height="19" rx="1.5"/><line x1="10" y1="18" x2="12" y2="18"/></svg>
    <span style="top:3px;">123 4567 8900</span>
  </div>
  <div class="contact contact-left" style="top:346px;">
    <svg viewBox="0 0 22 22" fill="none" stroke="#000" stroke-width="1.5"><path d="M5 2.5l3 3.5-1.8 2.2c1.2 2.8 3.6 5.2 6.4 6.4L14.8 13l3.7 3-1.8 3.3C9.5 19 3 12.5 2.7 5.3z"/></svg>
    <span style="top:3px;">123 4567 8900</span>
  </div>
  <div class="contact contact-left" style="top:391px;">
    <svg viewBox="0 0 22 22" fill="none" stroke="#000" stroke-width="1.5"><rect x="2" y="5" width="18" height="12"/><path d="M2 5l9 7 9-7M2 17l7-6M20 17l-7-6"/></svg>
    <span style="top:3px;">your@email.com</span>
  </div>

  <div class="contact contact-right" style="top:297px;">
    <svg viewBox="0 0 22 22" fill="none" stroke="#000" stroke-width="1.5"><path d="M11 21s-7-7.5-7-12.5a7 7 0 0 1 14 0C18 13.5 11 21 11 21z"/><circle cx="11" cy="8.5" r="2.5"/></svg>
    <span style="top:5px;">Your Address</span>
  </div>
  <div class="contact contact-right" style="top:346px;">
    <svg viewBox="0 0 22 22" fill="none" stroke="#000" stroke-width="1.5"><circle cx="11" cy="11" r="9.5"/><ellipse cx="11" cy="11" rx="4" ry="9.5"/><line x1="1.5" y1="11" x2="20.5" y2="11"/><line x1="3" y1="6" x2="19" y2="6"/><line x1="3" y1="16" x2="19" y2="16"/></svg>
    <span class="lower" style="top:3px;">www.websitelink.com</span>
  </div>
</section>

</body>
</html>
```